" Trabalho com uma abordagem integral, que tem uma visão para o fisico, mental, emocional e espiritual de mulheres na fase de climatério e menopausa e com o tratamento hormonal individualizado de cada uma delas. "

```html
<!DOCTYPE html>
<html lang="pt-BR">
<head>
<meta charset="UTF-8">
<title>Papel Timbrado — Dra. Helena Varela</title>
<link href="https://fonts.googleapis.com/css2?family=Cormorant+Garamond:wght@400;500&family=Montserrat:wght@400;500&display=swap" rel="stylesheet">
<style>
  :root {
    --backdrop: #8b786b;
    --paper: #ffffff;
    --gold: #b89a6c;
    --taupe: #a6968a;
    --muted: #a39890;
    --watermark: #f3f2f1;
    --footer-text: #ffffff;
  }
  * { margin: 0; padding: 0; box-sizing: border-box; }
  html, body {
    width: 1200px; height: 1200px; overflow: hidden;
    background: var(--backdrop);
  }
  .canvas { position: relative; width: 1200px; height: 1200px; }
  .letterhead {
    position: absolute; left: 348px; top: 228px;
    width: 504px; height: 744px;
    background: var(--paper);
    overflow: hidden;
    box-shadow: 0 6px 22px rgba(0,0,0,0.16);
  }
  .brand {
    position: absolute; top: 62px; left: 0; right: 0;
    display: flex; flex-direction: column; align-items: center;
  }
  .brand-row { display: flex; align-items: center; gap: 8px; }
  .brand-dot {
    width: 18px; height: 18px; border-radius: 50%;
    border: 1.3px solid var(--gold);
  }
  .brand-name-block { display: flex; flex-direction: column; line-height: 1; }
  .brand-title {
    font-family: "Cormorant Garamond", serif;
    font-weight: 500; font-size: 8px; color: var(--muted);
    margin-bottom: 2px;
  }
  .brand-name {
    font-family: "Cormorant Garamond", serif;
    font-weight: 500; font-size: 22px; color: var(--gold);
  }
  .brand-tagline {
    margin-top: 6px; margin-left: 26px;
    font-family: "Montserrat", sans-serif;
    font-size: 5px; letter-spacing: 1.2px; text-transform: uppercase;
    color: var(--muted);
  }
  .watermark-shape {
    position: absolute; left: 10px; top: 300px;
  }
  .footer-band {
    position: absolute; left: 0; bottom: 0; width: 504px; height: 56px;
  }
  .footer-shape { position: absolute; left: 0; top: 0; }
  .contact-list {
    position: absolute; left: 84px; right: 40px; bottom: 15px;
    display: flex; gap: 36px;
    font-family: "Montserrat", sans-serif; font-size: 7px;
    color: var(--footer-text); list-style: none;
  }
  .contact-item { display: flex; align-items: center; gap: 5px; white-space: nowrap; }
  .contact-icon { width: 10px; height: 10px; flex: none; }
</style>
</head>
<body>
<div class="canvas">
  <main class="letterhead">
    <svg class="watermark-shape" width="440" height="400" viewBox="0 0 440 400" aria-hidden="true">
      <circle cx="220" cy="200" r="180" fill="none" stroke="var(--watermark)" stroke-width="20"/>
    </svg>

    <header class="brand">
      <div class="brand-row">
        <span class="brand-dot"></span>
        <div class="brand-name-block">
          <span class="brand-title">Dra.</span>
          <span class="brand-name">Helena Varela</span>
        </div>
      </div>
      <p class="brand-tagline">Ginecologia e Saúde Integral da Mulher</p>
    </header>

    <footer class="footer-band">
      <svg class="footer-shape" width="504" height="56" viewBox="0 0 504 56" aria-hidden="true">
        <path d="M0 10 Q252 -4 504 10 L504 56 L0 56 Z" fill="var(--taupe)"/>
      </svg>
      <ul class="contact-list">
        <li class="contact-item">
          <svg class="contact-icon" viewBox="0 0 14 14" aria-hidden="true">
            <circle cx="7" cy="7" r="6.5" fill="#fff"/>
            <path d="M5 4 L6.3 4 L6.8 5.8 L6 6.4 Q6.8 8 8.2 8.6 L8.8 7.8 L10.4 8.3 L10.4 9.6 Q7.5 10 5.6 7.8 Q4.4 6 5 4 Z" fill="var(--taupe)"/>
          </svg>
          81 90000 1234
        </li>
        <li class="contact-item">
          <svg class="contact-icon" viewBox="0 0 14 14" aria-hidden="true">
            <circle cx="7" cy="7" r="6.5" fill="#fff"/>
            <rect x="3.5" y="4.5" width="7" height="5" fill="none" stroke="var(--taupe)" stroke-width="0.9"/>
            <path d="M3.5 4.8 L7 7.4 L10.5 4.8" fill="none" stroke="var(--taupe)" stroke-width="0.9"/>
          </svg>
          contato@helenavarela.med
        </li>
        <li class="contact-item">
          <svg class="contact-icon" viewBox="0 0 14 14" aria-hidden="true">
            <circle cx="7" cy="7" r="6.5" fill="#fff"/>
          </svg>
          @drahelenavarela
        </li>
      </ul>
    </footer>
  </main>
</div>
</body>
</html>
```